Re-design web project

1.Re-design of http://www.filmvonk-example.be
Logo		Ons concept 	Video referenties	Pagina delen	Promoot uw bedrijfsfilm
(Our concept)	(Video references)	(Share page)	(Promote yr company video)
Share-this buttons
Content promotion float
•	Bestel vandaag uw creatieve video en wij brengen hem vanaf 0,29 EUR onder de aandacht van potentiële klanten (Order today your creative video and we promote it online towards potential customers starting from € 0.29)
Slideshow images + content
•	Social Video = Online Video + Marketing + Social Media (Social Video = Online Video + Marketing + Social Media)
•	We verbeelden uw concept in een creatieve, aansprekende video (We visualise your concept into a creative video
•	We promoten uw video online en bereiken enkel potentiële klanten (We promote your video online and reach potential customers only)
•	Onbekende prospects worden kwalitatieve leads! (Unknown prospects are quality leads!)
Sketch + content
•	We stellen u een passend scenario voor (We propose an apropriate scenrio)
•	We visualiseren uw diensten (We visualize your services)
•	We brengen uw video onder de aandacht van potentiële klanten (We bring your video under the attention of potential customers)
•	We laten uw onderneming groeien! (We let your business grow!)
Bekijk onze video (Watch our video)
Ontvang vrijblijvend een presentatie van onze dienstverlening (Get a free presentation of our services )
Een aantal van onze video projecten (Take a look at our video projects)

Sitemap    Voorwaarden    Ons team    Contact
2. Re-design of http://www.filmvonk-example.be/luxe-appartement-centrum-gent as well

```html
<!DOCTYPE html>
<html lang="nl">
<head>
<meta charset="utf-8">
<title>FilmVonk – Social Video</title>
<link rel="stylesheet" href="https://fonts.googleapis.com/css2?family=Open+Sans:wdth,wght@75..100,300..700&family=Playfair+Display:ital@1&display=swap">
<style>
:root{
  --topbar:#464646;
  --topbar-line:#3a3a3a;
  --icon:#9a9a9a;
  --white:#ffffff;
  --brand:#5b93c6;
  --nav-text:#444444;
  --hero-top:#e4e4e2;
  --hero-bottom:#d9dad5;
  --script:#a9a9a6;
  --ink:#111111;
  --bar:#6b6b6b;
  --bar-active:#0c0c0c;
  --title:#555555;
  --body:#777777;
  --rule:#cfcfcf;
  --accent:#e58a5a;
  --arrow-bg:#eeeeee;
}
*{box-sizing:border-box;margin:0;padding:0}
html,body{width:1200px;height:1000px;overflow:hidden;background:var(--white)}
body{position:relative;font-family:"Open Sans",Arial,sans-serif;color:var(--nav-text)}

.topbar{position:absolute;left:0;top:0;width:1200px;height:55px;background:var(--topbar);border-bottom:1px solid var(--topbar-line)}
.share-list{position:absolute;right:188px;top:17px;display:flex;list-style:none}
.share-list li{width:34px;height:22px;display:flex;align-items:center;justify-content:center;border-left:1px dotted #6a6a6a}
.share-list li:first-child{border-left:none}
.share-dot{width:11px;height:11px;border-radius:2px;background:var(--icon)}

.site-header{position:absolute;left:0;top:56px;width:1200px;height:78px;background:var(--white)}
.logo{position:absolute;left:141px;top:20px;font-size:33px;font-weight:600;letter-spacing:-1.2px;color:var(--brand)}
.main-nav{position:absolute;right:201px;top:0;display:flex;list-style:none;height:78px}
.main-nav li{height:78px;display:flex;align-items:center;font-size:13px;padding:0 17px;color:var(--nav-text);white-space:nowrap}
.main-nav li:last-child{padding-right:5px}
.main-nav li.is-active{background:var(--brand);color:var(--white);width:72px;justify-content:center;padding:0;margin-right:2px}

.hero{position:absolute;left:0;top:134px;width:1200px;height:364px;background:linear-gradient(180deg,var(--hero-top),var(--hero-bottom))}
.hero-kicker{position:absolute;left:180px;top:130px;font-family:"Playfair Display",Georgia,serif;font-style:italic;font-size:36px;color:var(--script)}
.hero-title{position:absolute;left:97px;top:186px;font-weight:300;font-stretch:75%;font-size:64px;color:var(--ink);letter-spacing:-0.5px;white-space:nowrap}

.slide-pager{position:absolute;left:99px;top:498px;width:956px;height:12px;display:flex;gap:1px;box-shadow:0 2px 2px rgba(0,0,0,.15)}
.slide-pager span{flex:1;background:var(--bar)}
.slide-pager span.is-current{background:var(--bar-active)}

.features{position:absolute;left:143px;top:540px;width:870px;display:flex}
.feature{width:290px;text-align:center}
.feature-icon{height:55px;display:flex;align-items:center;justify-content:center}
.feature h3{margin-top:31px;font-weight:300;font-size:21px;color:var(--title)}
.feature p{margin:22px auto 0;width:236px;font-size:9.5px;line-height:17.5px;color:var(--body)}

.divider{position:absolute;left:154px;top:777px;width:845px;border-top:1px dotted var(--rule)}

.section-title{position:absolute;left:155px;top:823px;height:25px;border-left:2px dotted var(--accent);padding-left:9px;font-weight:300;font-size:20px;line-height:25px;color:var(--title)}
.carousel-nav{position:absolute;left:955px;top:826px;display:flex;gap:1px}
.carousel-nav span{width:22px;height:22px;background:var(--arrow-bg);display:flex;align-items:center;justify-content:center}

.projects{position:absolute;left:154px;top:866px;display:flex;gap:10px}
.project-thumb{width:204px;height:134px}
.thumb-1{background:linear-gradient(180deg,#c9c9c4 0,#8d8a82 45%,#5a4a3c 100%)}
.thumb-2{background:linear-gradient(180deg,#cacac2 0,#8e8e78 45%,#9a9a3a 100%)}
.thumb-3{background:linear-gradient(180deg,#cbc6c6 0,#8f8588 45%,#8c3550 100%)}
.thumb-4{background:linear-gradient(180deg,#c7c9cc 0,#868a94 45%,#34498a 100%)}
</style>
</head>
<body>
<div class="topbar">
  <ul class="share-list" aria-label="Pagina delen">
    <li><span class="share-dot"></span></li>
    <li><span class="share-dot"></span></li>
    <li><span class="share-dot"></span></li>
    <li><span class="share-dot"></span></li>
    <li><span class="share-dot"></span></li>
    <li><span class="share-dot"></span></li>
    <li><span class="share-dot"></span></li>
  </ul>
</div>

<header class="site-header">
  <div class="logo">FilmVonk</div>
  <ul class="main-nav">
    <li class="is-active">Home</li>
    <li>Ons concept</li>
    <li>Video referenties</li>
    <li>Pagina delen</li>
    <li>Promoot uw bedrijfsfilm</li>
  </ul>
</header>

<section class="hero" role="img" aria-label="Slideshow photo of young green sprouts against a pale grey background">
  <div class="hero-kicker">Online Video + Marketing</div>
  <div class="hero-title">SOCIAL VIDEO</div>
</section>

<div class="slide-pager">
  <span></span><span></span><span class="is-current"></span><span></span><span></span><span></span><span></span>
</div>

<section class="features">
  <article class="feature">
    <div class="feature-icon">
      <svg width="88" height="48" viewBox="0 0 88 48" fill="#5b93c6">
        <rect x="16" y="0" width="52" height="36" rx="3"/>
        <rect x="21" y="5" width="42" height="24" fill="#fff"/>
        <rect x="36" y="36" width="12" height="6"/><rect x="30" y="42" width="24" height="3"/>
        <rect x="0" y="14" width="26" height="34" rx="3"/><rect x="4" y="18" width="18" height="24" fill="#fff"/>
        <rect x="64" y="18" width="22" height="30" rx="3"/><rect x="67" y="22" width="16" height="20" fill="#fff"/>
      </svg>
    </div>
    <h3>Passend scenario</h3>
    <p>Samen met u werken we een scenario uit dat past bij uw bedrijf, uw doelgroep en uw boodschap.</p>
  </article>
  <article class="feature">
    <div class="feature-icon">
      <svg width="60" height="48" viewBox="0 0 60 48" fill="#5b93c6">
        <rect x="0" y="0" width="60" height="40" rx="5"/>
        <rect x="5" y="5" width="50" height="30" fill="#fff"/>
        <path d="M12 20l6-5v10zM48 20l-6-5v10z"/>
        <path d="M26 18h6v10h6v12H26z"/>
      </svg>
    </div>
    <h3>Creatieve video</h3>
    <p>We verbeelden uw concept en diensten in een creatieve, aansprekende video die blijft hangen bij uw klanten.</p>
  </article>
  <article class="feature">
    <div class="feature-icon">
      <svg width="70" height="48" viewBox="0 0 70 48" fill="#5b93c6">
        <circle cx="22" cy="20" r="14"/>
        <g stroke="#5b93c6" stroke-width="7">
          <path d="M22 0v40M2 20h40M8 6l28 28M36 6L8 34"/>
        </g>
        <circle cx="22" cy="20" r="6" fill="#fff"/>
        <circle cx="52" cy="32" r="9"/>
        <g stroke="#5b93c6" stroke-width="5">
          <path d="M52 19v26M39 32h26M43 23l18 18M61 23L43 41"/>
        </g>
        <circle cx="52" cy="32" r="4" fill="#fff"/>
      </svg>
    </div>
    <h3>Online promotie</h3>
    <p>We promoten uw video online en bereiken enkel potentiële klanten. Zo laten we uw onderneming groeien!</p>
  </article>
</section>

<div class="divider"></div>

<h2 class="section-title">Onze video projecten</h2>
<div class="carousel-nav">
  <span><svg width="8" height="10" viewBox="0 0 8 10"><path d="M6 1L2 5l4 4" stroke="#bbb" fill="none" stroke-width="1.5"/></svg></span>
  <span><svg width="8" height="10" viewBox="0 0 8 10"><path d="M2 1l4 4-4 4" stroke="#bbb" fill="none" stroke-width="1.5"/></svg></span>
</div>

<div class="projects">
  <div class="project-thumb thumb-1" role="img" aria-label="Video still of a bright apartment living room with tall windows and wooden floor"></div>
  <div class="project-thumb thumb-2" role="img" aria-label="Video still of the same living room with a green tinted floor"></div>
  <div class="project-thumb thumb-3" role="img" aria-label="Video still of the same living room with a red tinted floor"></div>
  <div class="project-thumb thumb-4" role="img" aria-label="Video still of the same living room with a blue tinted floor"></div>
</div>
</body>
</html>
```